MAREK DOLVANE FOR CONGRESS DISTRICT 32

I need to create a campaign flyer for my congress campaign. I am running for congress in District 32 of Texas as a republican. I am a former Olympic athlete, world champion fencer, Army veteran, Counterintelligence officer (I catch spies).
I want just my first name MAREK in big letters at the top. I want it to say MAREK and below it Republican for Congress.
www.marekforcongress.example

Industry/Entity Type

Political

Colors
EB3D1F
EC4F4E
F09395
F8D3D4
FCEDEE

Requirements
Nice to have
• Would love a catchy title for the Flyer like "Spy Catcher", "Olympic Athlete" "World Champion Fencer" running for Congress in your District!

```html
<!DOCTYPE html>
<html lang="en">
<head>
<meta charset="utf-8">
<title>Marek for Congress Flyer</title>
<link href="https://fonts.googleapis.com/css2?family=Bebas+Neue&family=Montserrat:wght@700;800;900&display=swap" rel="stylesheet">
<style>
  :root {
    --backdrop: #e5e5e5;
    --blue-bright: #1a2cf0;
    --blue-mid: #0d17c4;
    --navy: #0a0a5c;
    --night: #12002a;
    --red: #e0141b;
    --white: #ffffff;
    --text-blue: #0b0fb0;
    --photo-light: #c9c6e6;
    --photo-mid: #7d7ac8;
  }
  * { box-sizing: border-box; margin: 0; padding: 0; }
  html, body { width: 1200px; height: 1200px; overflow: hidden; background: var(--backdrop); }
  .flyer {
    position: absolute; left: 268px; top: 130px; width: 664px; height: 938px;
    background: var(--white); overflow: hidden;
  }
  .hero {
    position: absolute; left: 0; top: 0; width: 664px; height: 663px;
    background:
      radial-gradient(ellipse 60% 45% at 45% 45%, rgba(40,60,255,.9), transparent 70%),
      linear-gradient(135deg, var(--blue-bright) 0%, var(--blue-mid) 40%, var(--navy) 75%, var(--night) 100%);
  }
  .headline { position: absolute; left: 0; top: 0; width: 664px; height: 240px; }
  .headline text { font-family: 'Montserrat', sans-serif; font-weight: 800; fill: var(--white); }
  .party-banner {
    position: absolute; left: 65px; top: 235px; width: 527px; height: 57px; background: var(--red);
  }
  .party-banner text { font-family: 'Bebas Neue', sans-serif; fill: var(--white); }
  .credentials { position: absolute; left: 63px; top: 305px; list-style: none; }
  .credentials li {
    display: flex; align-items: center; height: 52px; gap: 8px;
    font-family: 'Montserrat', sans-serif; font-weight: 800; font-size: 35px; color: var(--white);
    text-shadow: 0 2px 4px rgba(0,0,20,.5); letter-spacing: .5px;
  }
  .credentials svg { width: 31px; height: 31px; flex: none; }
  .photo-action {
    position: absolute; left: 45px; top: 469px; width: 200px; height: 194px;
    background: linear-gradient(160deg, var(--photo-mid), var(--photo-light));
    border-radius: 90px 90px 0 0; opacity: .75;
  }
  .photo-portrait {
    position: absolute; left: 353px; top: 304px; width: 311px; height: 359px;
    background: linear-gradient(180deg, #8a6f66 0%, #c9a89a 35%, #e8e8ee 70%, #f4f4f8 100%);
    border-radius: 150px 150px 0 0;
  }
  .flag-band { position: absolute; left: 0; top: 663px; width: 664px; height: 40px; }
  .pitch { position: absolute; left: 0; top: 703px; width: 664px; height: 235px; }
  .pitch .title { font-family: 'Bebas Neue', sans-serif; fill: var(--text-blue); }
  .pitch .subtitle { font-family: 'Montserrat', sans-serif; font-weight: 800; fill: var(--red); }
  .pitch .district { font-family: 'Montserrat', sans-serif; font-weight: 800; fill: var(--white); }
</style>
</head>
<body>
<main class="flyer">
  <section class="hero">
    <svg class="headline" viewBox="0 0 664 240">
      <defs>
        <filter id="lift" x="-5%" y="-5%" width="110%" height="115%">
          <feDropShadow dx="0" dy="3" stdDeviation="3" flood-color="#000030" flood-opacity=".6"/>
        </filter>
      </defs>
      <text x="65" y="232" font-size="205" textLength="527" lengthAdjust="spacingAndGlyphs" filter="url(#lift)">MAREK</text>
      <polygon points="400,22 409,48 437,48 414,64 423,91 400,74 377,91 386,64 363,48 391,48"
               fill="var(--white)" stroke="var(--red)" stroke-width="4" stroke-linejoin="round"/>
    </svg>

    <svg class="party-banner" viewBox="0 0 527 57">
      <text x="263.5" y="49" font-size="58" text-anchor="middle" textLength="505" lengthAdjust="spacingAndGlyphs">REPUBLICAN FOR CONGRESS</text>
    </svg>

    <ul class="credentials">
      <li><svg viewBox="0 0 32 32"><circle cx="15" cy="17" r="12" fill="none" stroke="#fff" stroke-width="4"/><path d="M9 16l5 6L28 5" fill="none" stroke="#fff" stroke-width="4.5" stroke-linecap="round" stroke-linejoin="round"/></svg>VETERAN</li>
      <li><svg viewBox="0 0 32 32"><circle cx="15" cy="17" r="12" fill="none" stroke="#fff" stroke-width="4"/><path d="M9 16l5 6L28 5" fill="none" stroke="#fff" stroke-width="4.5" stroke-linecap="round" stroke-linejoin="round"/></svg>OLYMPIAN</li>
      <li><svg viewBox="0 0 32 32"><circle cx="15" cy="17" r="12" fill="none" stroke="#fff" stroke-width="4"/><path d="M9 16l5 6L28 5" fill="none" stroke="#fff" stroke-width="4.5" stroke-linecap="round" stroke-linejoin="round"/></svg>LEADER</li>
    </ul>

    <div class="photo-action" role="img" aria-label="Photo of the candidate fencing in competition whites, shouting in celebration"></div>
    <div class="photo-portrait" role="img" aria-label="Smiling head-and-shoulders portrait of the candidate in a white shirt"></div>
  </section>

  <svg class="flag-band" viewBox="0 0 664 40" preserveAspectRatio="none">
    <rect width="664" height="40" fill="var(--white)"/>
    <rect x="110" y="0" width="554" height="5" fill="var(--red)"/>
    <rect x="110" y="11" width="554" height="5" fill="var(--red)"/>
    <rect x="110" y="23" width="554" height="5" fill="var(--red)"/>
    <rect x="110" y="35" width="554" height="5" fill="var(--red)"/>
    <rect x="0" y="0" width="110" height="40" fill="var(--text-blue)"/>
    <g fill="var(--white)">
      <polygon points="20,9 23,17 31,17 25,22 27,30 20,25 13,30 15,22 9,17 17,17"/>
      <polygon points="55,9 58,17 66,17 60,22 62,30 55,25 48,30 50,22 44,17 52,17"/>
      <polygon points="90,9 93,17 101,17 95,22 97,30 90,25 83,30 85,22 79,17 87,17"/>
    </g>
  </svg>

  <svg class="pitch" viewBox="0 0 664 235">
    <defs>
      <linearGradient id="pill" x1="0" x2="1">
        <stop offset="0" stop-color="var(--red)"/>
        <stop offset=".35" stop-color="var(--red)"/>
        <stop offset="1" stop-color="var(--text-blue)"/>
      </linearGradient>
    </defs>
    <text class="title" x="332" y="98" font-size="100" text-anchor="middle" textLength="548" lengthAdjust="spacingAndGlyphs">OLYMPIC ATHLETE</text>
    <text class="subtitle" x="332" y="148" font-size="41" text-anchor="middle" textLength="538" lengthAdjust="spacingAndGlyphs">RUNNING FOR CONGRESS</text>
    <rect x="136" y="160" width="401" height="45" rx="9" fill="url(#pill)"/>
    <text class="district" x="336" y="195" font-size="34" text-anchor="middle" textLength="370" lengthAdjust="spacingAndGlyphs">IN YOUR DISTRICT!</text>
  </svg>
</main>
</body>
</html>
```